Harrowgate Supply Group Business Card Design

The Business Card will be one side only with Harrowgate Supplies Group Logo
Card should have:
Name
Title
Office phone Number
Cell Number
email address
Website
Street Address
Our Slogan is Rugged and Reliable
Looking for something that stands out from other business cards

Target Market(s)

Heavy equipment Lease Company

```html
<!DOCTYPE html>
<html lang="en">
<head>
<meta charset="utf-8">
<title>Harrowgate Supply Group Business Card</title>
<link href="https://fonts.googleapis.com/css2?family=Arimo:wght@400;700&display=swap" rel="stylesheet">
<style>
  :root {
    --navy: #262a72;
    --red: #d2152c;
    --white: #ffffff;
    --ink: #1d1d1f;
    --backdrop: #e4ddd3;
  }
  * { margin: 0; padding: 0; box-sizing: border-box; }
  html, body {
    width: 1200px; height: 1200px; overflow: hidden;
    background: var(--backdrop);
    font-family: "Arimo", Arial, sans-serif;
  }
  .canvas { position: relative; width: 1200px; height: 1200px; }

  .card {
    position: absolute; left: 240px; width: 720px; height: 412px;
    border-radius: 16px; overflow: hidden;
    box-shadow: 0 6px 16px rgba(0,0,0,0.18);
  }

  /* Front */
  .card-front { top: 146px; background: var(--navy); }
  .card-front .edge {
    position: absolute; left: 0; right: 0; bottom: 0; height: 6px; background: var(--red);
  }
  .front-brand {
    position: absolute; left: 0; right: 0; top: 172px;
    display: flex; justify-content: center; align-items: center; gap: 20px;
  }
  .brand-dot { width: 34px; height: 34px; border-radius: 50%; background: var(--red); flex: none; }
  .front-brand .brand-name {
    color: var(--white); font-weight: 700; font-size: 34px; letter-spacing: 0.5px;
  }
  .tagline {
    position: absolute; left: 0; right: 0; top: 366px; text-align: center;
    color: var(--white); font-weight: 700; font-size: 16px; letter-spacing: 2.2px;
  }

  /* Back */
  .card-back { top: 642px; background: var(--white); }
  .back-brand {
    position: absolute; left: 28px; top: 70px;
    display: flex; align-items: center; gap: 12px;
  }
  .back-brand .brand-dot { width: 26px; height: 26px; }
  .back-brand .brand-name {
    color: var(--red); font-weight: 700; font-size: 23px; letter-spacing: 0.3px;
  }
  .person { position: absolute; left: 136px; top: 190px; }
  .person-name { color: var(--navy); font-weight: 700; font-size: 28px; letter-spacing: 0.6px; line-height: 1; }
  .person-title { color: var(--ink); font-size: 17px; margin-top: 8px; }

  .contacts { position: absolute; left: 136px; top: 284px; list-style: none; }
  .contacts li {
    display: flex; align-items: center; gap: 10px;
    color: var(--ink); font-size: 17px; letter-spacing: 0.3px; height: 22.5px;
  }
  .contacts svg { width: 14px; height: 14px; fill: var(--red); flex: none; }

  .address {
    position: absolute; left: 514px; top: 282px;
    color: var(--ink); font-size: 15.5px; line-height: 19px;
  }
  .band { position: absolute; bottom: 0; height: 6px; }
  .band-navy { left: 0; width: 510px; background: var(--navy); }
  .band-red { left: 514px; right: 0; background: var(--red); }
</style>
</head>
<body>
<div class="canvas">

  <section class="card card-front">
    <div class="front-brand">
      <span class="brand-dot"></span>
      <span class="brand-name">HARROWGATE SUPPLIES GROUP</span>
    </div>
    <p class="tagline">RUGGED AND RELIABLE</p>
    <div class="edge"></div>
  </section>

  <section class="card card-back">
    <div class="back-brand">
      <span class="brand-dot"></span>
      <span class="brand-name">HARROWGATE SUPPLIES GROUP</span>
    </div>

    <div class="person">
      <h1 class="person-name">DANIEL CARVER</h1>
      <p class="person-title">Director</p>
    </div>

    <ul class="contacts">
      <li>
        <svg viewBox="0 0 14 14" aria-hidden="true"><path d="M3.5 0h7a1 1 0 0 1 1 1v12a1 1 0 0 1-1 1h-7a1 1 0 0 1-1-1V1a1 1 0 0 1 1-1zm.8 1.8v8.6h5.4V1.8zM7 11.2a.9.9 0 1 0 0 1.8.9.9 0 0 0 0-1.8z"/></svg>
        555 214 7380
      </li>
      <li>
        <svg viewBox="0 0 14 14" aria-hidden="true"><path d="M3 .5l2.2 2.8-1.3 1.6c.9 2 2.4 3.5 4.4 4.4l1.6-1.3L12.7 10l-1.2 2.6C6 12.4 1.6 8 1.4 2.5z"/></svg>
        555 386 9102
      </li>
      <li>
        <svg viewBox="0 0 14 14" aria-hidden="true"><path d="M0 3h14v1.2L7 8.2 0 4.2zM0 5.6l7 4 7-4V11H0z"/></svg>
        info@harrowgatesupply.com
      </li>
      <li>
        <svg viewBox="0 0 14 14" aria-hidden="true"><path d="M7 .5a6.5 6.5 0 1 0 0 13 6.5 6.5 0 0 0 0-13zm0 1.3c.8.7 1.4 2 1.6 3.5H5.4C5.6 3.8 6.2 2.5 7 1.8zM1.9 6.5h2.3v1H1.9zm0 0M5.3 6.5h3.4v1H5.3zm4.5 0h2.3v1H9.8zM5.4 8.7h3.2C8.4 10.2 7.8 11.4 7 12.2c-.8-.8-1.4-2-1.6-3.5z"/></svg>
        www.harrowgatesupply.com
      </li>
    </ul>

    <address class="address" style="font-style:normal">
      48213<br>
      W. Granite Ridge Rd Ste. B<br>
      Millbrook, TX 75920
    </address>

    <div class="band band-navy"></div>
    <div class="band band-red"></div>
  </section>

</div>
</body>
</html>
```